Preferred pricing vendor

We are a plumbing company that has many services
-Boilers & Controls
-Plumbing & Heating
-HVAC & Refrigeration
-Preventative Maintenacne
-Gas fitting & Drain Cleaning

We primarily look after condo buildings, and our preferred service rates ($98, $93, or $88 depending on the contract) extend to all of our clients. So in essence, we look after the mechanical room and common equipment but our clients can call us in for drain cleaning or replacing a fixture in their suite. The discounted rates apply to the personal residence. We want a flyer to let them know they get a discount on our services. A one-pager we can send out to all of our contract clients.

Included source files for our letterhead and logo just so you can see the colours we go with.

Target Market(s)

Residential repairs, individual people, replacement of fixtures in-suite specific repairs

Requirements
Must have
• be colourful and attractive

```html
<!DOCTYPE html>
<html lang="en">
<head>
<meta charset="utf-8">
<title>Keystone Mechanical Inc – Preferred Service Rates</title>
<link rel="stylesheet" href="https://fonts.googleapis.com/css2?family=Krona+One&family=Roboto:wght@500&family=Roboto+Condensed:wght@500;700&family=Open+Sans:wght@400&display=swap">
<style>
  :root {
    --brand-blue: #2b6cb8;
    --brand-orange: #ef5a24;
    --ink: #1d1d1f;
    --paper: #ffffff;
    --stage: #e9edf2;
    --rule: #c9d3e6;
    --icon-tint: #d7eef3;
    --muted: #333;
  }
  * { margin: 0; padding: 0; box-sizing: border-box; }
  html, body { width: 1200px; height: 1200px; overflow: hidden; background: var(--stage); }
  .stage { position: relative; width: 1200px; height: 1200px; }
  .flyer {
    position: absolute; left: 159px; top: 30px;
    width: 936px; height: 1210px;
    background: var(--paper);
    transform: scale(0.942); transform-origin: top left;
    overflow: hidden;
  }
  .brand {
    position: absolute; left: 60px; top: 150px; width: 340px;
    display: flex; align-items: center; justify-content: center; gap: 14px;
  }
  .brand-dot { width: 40px; height: 40px; border-radius: 50%; background: var(--brand-orange); flex: none; }
  .brand-name {
    font-family: "Roboto Condensed", sans-serif; font-weight: 700;
    color: var(--brand-blue); font-size: 38px; line-height: 1; text-transform: uppercase;
  }
  .hero-photo { position: absolute; left: 0; top: 0; width: 936px; height: 560px; }
  .headline-box {
    position: absolute; left: 32px; top: 300px; width: 640px; height: 216px;
    background: var(--brand-blue); border-radius: 16px 0 0 16px;
  }
  .headline {
    position: absolute; left: 82px; top: 326px; z-index: 2;
    font-family: "Krona One", sans-serif; font-weight: 400; color: #fff;
    font-size: 33px; line-height: 41px;
  }
  .rates {
    position: absolute; left: 83px; top: 538px;
    font-family: "Roboto", sans-serif; font-weight: 500;
    color: var(--brand-blue);
  }
  .rates-title { font-size: 23px; line-height: 28px; }
  .rates-detail { font-size: 20px; line-height: 26px; }
  .services { position: absolute; left: 0; top: 612px; width: 936px; list-style: none; }
  .service { position: relative; height: 87.5px; }
  .service-icon {
    position: absolute; left: 74px; top: 8px; width: 88px; height: 72px;
    border-radius: 10px; background: linear-gradient(135deg, var(--icon-tint), #f3d9cf);
  }
  .service-label {
    position: absolute; left: 204px; top: 25px;
    font-family: "Krona One", sans-serif; font-size: 30px; color: var(--ink); white-space: nowrap;
  }
  .service:not(:last-child)::after {
    content: ""; position: absolute; left: 204px; right: 74px; bottom: 0; height: 2px;
    background: linear-gradient(90deg, var(--rule), rgba(201,211,230,0.2));
  }
  .cta {
    position: absolute; left: 0; top: 1050px; width: 936px;
    display: flex; align-items: center; gap: 10px;
  }
  .cta::before, .cta::after { content: ""; flex: 1; height: 3px; background: var(--brand-blue); }
  .cta-text {
    font-family: "Roboto Condensed", sans-serif; font-weight: 700;
    color: var(--brand-orange); font-size: 27px; letter-spacing: 0.2px;
  }
  .footer-brand {
    position: absolute; left: 66px; top: 1108px; width: 270px;
    display: flex; align-items: center; gap: 12px;
  }
  .footer-brand .brand-dot { width: 34px; height: 34px; }
  .footer-brand .brand-name { font-size: 24px; line-height: 25px; }
  .footer-divider { position: absolute; top: 1096px; width: 3px; height: 72px; background: var(--brand-blue); }
  .address {
    position: absolute; left: 383px; top: 1098px; font-style: normal;
    font-family: "Open Sans", sans-serif; font-size: 17px; line-height: 24px; color: var(--muted);
  }
  .contacts {
    position: absolute; left: 644px; top: 1092px; list-style: none;
    font-family: "Open Sans", sans-serif; font-size: 17px; line-height: 25px; color: var(--muted);
  }
  .contacts li { display: flex; align-items: center; gap: 6px; }
  .contacts svg { width: 16px; height: 16px; flex: none; }
  .band { position: absolute; top: 1178px; height: 32px; }
  .band-blue { left: 0; width: 618px; background: var(--brand-blue); }
  .band-orange { left: 626px; width: 310px; background: var(--brand-orange); }
</style>
</head>
<body>
<main class="stage">
  <article class="flyer">
    <svg class="hero-photo" viewBox="0 0 936 560">
      <defs>
        <clipPath id="hero-clip"><circle cx="746" cy="236" r="301"/></clipPath>
        <linearGradient id="hero-tone" x1="0" y1="0" x2="1" y2="1">
          <stop offset="0" stop-color="#eef1f4"/>
          <stop offset="0.45" stop-color="#3a5fa8"/>
          <stop offset="1" stop-color="#1f3f86"/>
        </linearGradient>
      </defs>
      <g role="img" aria-label="Photo of a plumber in blue overalls holding a pipe wrench, with a plunger and tools on his belt">
        <rect x="0" y="-80" width="936" height="640" fill="url(#hero-tone)" clip-path="url(#hero-clip)"/>
      </g>
      <circle cx="746" cy="236" r="301" fill="none" stroke="var(--brand-orange)" stroke-width="8"/>
    </svg>

    <div class="brand">
      <span class="brand-dot"></span>
      <span class="brand-name">Keystone Mechanical Inc</span>
    </div>

    <div class="headline-box"></div>
    <h1 class="headline">Professional<br>Plumbers<br>at your<br>service 24 hours</h1>

    <div class="rates">
      <p class="rates-title">Preferred service rates</p>
      <p class="rates-detail">($98, $93, or $88 depending on the contract) extend to all of our clients.</p>
    </div>

    <ul class="services">
      <li class="service"><span class="service-icon" role="img" aria-label="Icon of pipe fittings with gauge and valve"></span><span class="service-label">Boilers &amp; Controls</span></li>
      <li class="service"><span class="service-icon" role="img" aria-label="Icon of a plumber's toolbox"></span><span class="service-label">Plumbing &amp; Heating</span></li>
      <li class="service"><span class="service-icon" role="img" aria-label="Icon of a heating radiator"></span><span class="service-label">HVAC &amp; Refrigeration</span></li>
      <li class="service"><span class="service-icon" role="img" aria-label="Icon of pipes with a wrench"></span><span class="service-label">Preventative Maintenacne</span></li>
      <li class="service"><span class="service-icon" role="img" aria-label="Icon of a gas valve and hand with wrench"></span><span class="service-label">Gas fitting &amp; Drain Cleaning</span></li>
    </ul>

    <div class="cta"><span class="cta-text">SPECIAL DISCOUNT CALL US NOW</span></div>

    <div class="footer-brand">
      <span class="brand-dot"></span>
      <span class="brand-name">Keystone<br>Mechanical Inc</span>
    </div>
    <span class="footer-divider" style="left:356px"></span>
    <address class="address">2180 Harbor Crest Avenue,<br>Suite 210 Bayview.</address>
    <span class="footer-divider" style="left:617px"></span>
    <ul class="contacts">
      <li><svg viewBox="0 0 16 16"><path d="M4 2l3 3-2 2c1 2 2 3 4 4l2-2 3 3-2 2C7 14 2 9 2 4z" fill="var(--brand-orange)"/></svg>555.214.0198</li>
      <li><svg viewBox="0 0 16 16"><rect x="1" y="3" width="14" height="10" fill="var(--brand-orange)"/><path d="M1 3l7 6 7-6" fill="none" stroke="#fff" stroke-width="1.5"/></svg>info@keystonemech.com</li>
      <li><svg viewBox="0 0 16 16"><circle cx="8" cy="8" r="7" fill="var(--brand-orange)"/><path d="M1 8h14M8 1c-3 4-3 10 0 14M8 1c3 4 3 10 0 14" fill="none" stroke="#fff" stroke-width="1"/></svg>www.keystonemech.com</li>
    </ul>

    <div class="band band-blue"></div>
    <div class="band band-orange"></div>
  </article>
</main>
</body>
</html>
```